Tidal Coatings business card for residential and commercial painting

A clean, professional design. Easy to read
Eye catching and elegant
Front could have some color variations
On the back of card I would like all black with signature logo

*Attached is my current business card and the items I want displayed

Contact Information for Business Card

Email, phone number, website, and owner name

Font styles to use
Serif

Requirements
Must have
• My logo with cool design and perhaps some paint splatter

```html
<!DOCTYPE html>
<html lang="en">
<head>
<meta charset="utf-8">
<title>Tidal Coatings – Business Card</title>
<link href="https://fonts.googleapis.com/css2?family=Playfair+Display:wght@600&family=Source+Serif+4:wght@400&display=swap" rel="stylesheet">
<style>
  :root {
    --stage: #c4c4c4;
    --brand-blue: #1076be;
    --charcoal: #3a3a3c;
    --black: #111111;
    --white: #ffffff;
    --brush-light: #ffffff;
    --brush-shade: #e4e8ec;
  }
  * { margin: 0; padding: 0; box-sizing: border-box; }
  html, body {
    width: 1093px;
    height: 1200px;
    overflow: hidden;
    background: var(--stage);
  }
  .canvas {
    position: relative;
    width: 1093px;
    height: 1200px;
  }
  .card {
    position: absolute;
    left: 264px;
    width: 580px;
    height: 358px;
    overflow: hidden;
  }
  .card--front { top: 226px; background: var(--brand-blue); }
  .card--back { top: 620px; background: var(--black); }

  .front__panel {
    position: absolute;
    left: 0; top: 0;
    width: 140px; height: 100%;
    background: var(--charcoal);
  }
  .front__brush {
    position: absolute;
    left: 92px; top: 0;
    width: 88px; height: 352px;
    border-radius: 40px 40px 6px 6px;
    background: linear-gradient(180deg, var(--brush-light) 0%, var(--brush-shade) 100%);
  }

  .wordmark {
    position: absolute;
    font-family: "Playfair Display", serif;
    font-weight: 600;
    line-height: 1;
    white-space: nowrap;
    color: var(--white);
  }
  .wordmark--front { left: 213px; top: 66px; font-size: 34px; }
  .wordmark--back { left: 36px; top: 74px; font-size: 36px; }

  .owner {
    position: absolute;
    left: 215px; top: 190px;
    color: var(--white);
  }
  .owner__name {
    font-family: "Playfair Display", serif;
    font-weight: 600;
    font-size: 26px;
    line-height: 1.15;
  }
  .owner__title {
    font-family: "Source Serif 4", serif;
    font-size: 16px;
    line-height: 1.3;
  }

  .contact {
    position: absolute;
    left: 215px; top: 258px;
    list-style: none;
    color: var(--white);
    font-family: "Source Serif 4", serif;
    font-size: 15.5px;
  }
  .contact__item {
    display: flex;
    align-items: center;
    height: 21px;
  }
  .contact__icon {
    width: 17px; height: 17px;
    margin-right: 10px;
    flex: none;
  }
</style>
</head>
<body>
<main class="canvas">
  <section class="card card--front" aria-label="Business card front">
    <div class="front__panel"></div>
    <div class="front__brush" role="img" aria-label="Large white paintbrush illustration with dripping paint"></div>

    <div class="wordmark wordmark--front">TIDAL COATINGS</div>

    <div class="owner">
      <p class="owner__name">Marcus "Mac"</p>
      <p class="owner__title">Owner-Licensed &amp; Insured</p>
    </div>

    <ul class="contact">
      <li class="contact__item">
        <svg class="contact__icon" viewBox="0 0 24 24" aria-hidden="true">
          <path fill="var(--white)" d="M6.6 10.8a15.1 15.1 0 0 0 6.6 6.6l2.2-2.2a1 1 0 0 1 1-.25 11.4 11.4 0 0 0 3.6.57 1 1 0 0 1 1 1V20a1 1 0 0 1-1 1A17 17 0 0 1 3 4a1 1 0 0 1 1-1h3.5a1 1 0 0 1 1 1c0 1.25.2 2.45.57 3.57a1 1 0 0 1-.25 1z"/>
        </svg>
        555.201.4378
      </li>
      <li class="contact__item">
        <svg class="contact__icon" viewBox="0 0 24 24" aria-hidden="true">
          <rect x="2" y="5" width="20" height="14" fill="var(--white)"/>
          <path d="M2 5l10 8 10-8M2 19l7.5-7M22 19l-7.5-7" fill="none" stroke="var(--brand-blue)" stroke-width="1.5"/>
        </svg>
        info@tidalcoatings.com
      </li>
      <li class="contact__item">
        <svg class="contact__icon" viewBox="0 0 24 24" aria-hidden="true">
          <g fill="none" stroke="var(--white)" stroke-width="1.6">
            <circle cx="12" cy="12" r="9.5"/>
            <ellipse cx="12" cy="12" rx="4.5" ry="9.5"/>
            <path d="M2.5 12h19M4 7h16M4 17h16M12 2.5v19"/>
          </g>
        </svg>
        www.tidalcoatings.com
      </li>
    </ul>
  </section>

  <section class="card card--back" aria-label="Business card back">
    <div class="wordmark wordmark--back">TIDAL COATINGS</div>
  </section>
</main>
</body>
</html>
```